Bright Fern Custom Homes business card. Double sided. Modern. professional

Bright Fern Custom Homes
contemporary modern design with our logo /
Double sided with all our contact information
Use same Green colors as in our Logo. Contemporary logo that grabs your attention. Visually pleasing and balanced. Easy to read, and Vibrant. Would love an option for rounded edges. Embossed logo would be amazing.
Contact Information for Business Card
Dana Welk Owner / General Contractor Bright Fern Custom Homes p: 704.552.1830 m: 912.648.2071 e: brightferncustomhomes@mailbox.example w: www.brightferncustomhomes.example 218 Pryor Meadow Lane Alder Falls, OR 97041

```html
<!DOCTYPE html>
<html lang="en">
<head>
<meta charset="utf-8">
<title>Bright Fern Custom Homes – Business Card</title>
<link rel="stylesheet" href="https://fonts.googleapis.com/css2?family=Quicksand:wght@500;600&family=Source+Sans+3:wght@800&display=swap">
<style>
  :root {
    --page-bg: #e9ecdf;
    --card-cream: #eef2e0;
    --fern: #6e8c35;
    --fern-dark: #5f7a2c;
    --ink: #3a3a36;
    --white: #ffffff;
  }
  * { box-sizing: border-box; margin: 0; padding: 0; }
  html, body {
    width: 1200px; height: 1200px; overflow: hidden;
    background: var(--page-bg);
  }
  .card {
    position: absolute; left: 220px;
    width: 760px; height: 433px;
    border-radius: 22px;
    overflow: hidden;
    box-shadow: 0 8px 24px rgba(40, 55, 20, 0.18);
  }
  .card--front { top: 137px; background: var(--card-cream); }
  .card--back  { top: 630px; background: var(--fern); color: var(--white); }

  .rule { position: absolute; background: var(--fern); }

  .person-name {
    position: absolute; left: 65px; top: 100px;
    font: 800 37px/1 "Source Sans 3", sans-serif;
    color: var(--fern);
  }
  .person-role {
    position: absolute; left: 66px; top: 150px;
    font: 500 19px/28px "Quicksand", sans-serif;
    color: var(--ink);
  }
  .contact-list { position: absolute; left: 62px; top: 276px; list-style: none; }
  .contact-item {
    display: flex; align-items: center; height: 29px; margin-bottom: 10.5px;
    font: 500 22px/1 "Quicksand", sans-serif; color: var(--ink);
    white-space: nowrap;
  }
  .contact-icon {
    width: 29px; height: 29px; border-radius: 50%;
    background: var(--fern); margin-right: 17px; flex: none;
    display: flex; align-items: center; justify-content: center;
  }
  .contact-sep { margin: 0 16px; font-size: 14px; }

  .brand { position: absolute; text-align: center; font-family: "Quicksand", sans-serif; font-weight: 600; }
  .brand-dot { display: block; margin: 0 auto; border-radius: 50%; }
  .brand-name { display: block; letter-spacing: 0.06em; text-transform: uppercase; white-space: nowrap; }
  .brand-sub { display: block; text-transform: uppercase; white-space: nowrap; }

  .brand--front { left: 460px; top: 52px; width: 240px; color: var(--fern); }
  .brand--front .brand-dot { width: 110px; height: 110px; background: var(--fern); margin-bottom: 20px; }
  .brand--front .brand-name { font-size: 28px; line-height: 1; }
  .brand--front .brand-sub { font-size: 9px; letter-spacing: 0.6em; margin-top: 3px; }

  .brand--back { left: 0; top: 48px; width: 760px; color: var(--white); }
  .brand--back .brand-dot { width: 190px; height: 190px; background: var(--white); margin-bottom: 30px; }
  .brand--back .brand-name { font-size: 52px; line-height: 1; }
  .brand--back .brand-sub { font-size: 12px; letter-spacing: 0.8em; margin-top: 4px; }

  .website {
    position: absolute; left: 0; top: 358px; width: 760px; text-align: center;
    font: 600 19px/1 "Quicksand", sans-serif; letter-spacing: 0.09em; color: var(--white);
  }
</style>
</head>
<body>

<section class="card card--front">
  <span class="rule" style="left:31px;top:51px;width:283px;height:2px"></span>
  <span class="rule" style="left:64px;top:0;width:2px;height:67px"></span>
  <span class="rule" style="left:281px;top:0;width:2px;height:67px"></span>

  <h1 class="person-name">Dana Welk</h1>
  <p class="person-role">Owner / General Contractor<br>Bright Fern Custom Homes</p>
  <span class="rule" style="left:65px;top:237px;width:119px;height:2px"></span>

  <ul class="contact-list">
    <li class="contact-item">
      <span class="contact-icon">
        <svg width="15" height="15" viewBox="0 0 24 24"><path fill="#fff" d="M6.6 10.8a15 15 0 0 0 6.6 6.6l2.2-2.2a1 1 0 0 1 1-.25 11.4 11.4 0 0 0 3.6.57 1 1 0 0 1 1 1V20a1 1 0 0 1-1 1A17 17 0 0 1 3 4a1 1 0 0 1 1-1h3.5a1 1 0 0 1 1 1c0 1.250.2 2.450.57 3.570a1 1 0 0 1-.25 1z"/></svg>
      </span>
      p. 704.552.1830<span class="contact-sep">●</span>m. 912.648.2071
    </li>
    <li class="contact-item">
      <span class="contact-icon">
        <svg width="15" height="15" viewBox="0 0 24 24"><rect x="3" y="5" width="18" height="14" rx="2" fill="none" stroke="#fff" stroke-width="2"/><path d="M3.5 6.5 12 13l8.5-6.5" fill="none" stroke="#fff" stroke-width="2"/></svg>
      </span>
      brightferncustomhomes@mailbox.example
    </li>
    <li class="contact-item">
      <span class="contact-icon">
        <svg width="15" height="15" viewBox="0 0 24 24"><path fill="#fff" d="M12 2a7 7 0 0 0-7 7c0 5 7 13 7 13s7-8 7-13a7 7 0 0 0-7-7zm0 9.5A2.5 2.5 0 1 1 12 6.5a2.5 2.5 0 0 1 0 5z"/></svg>
      </span>
      218 Pryor Meadow Lane Alder Falls, OR 97041
    </li>
  </ul>

  <div class="brand brand--front">
    <span class="brand-dot"></span>
    <span class="brand-name">Bright Fern</span>
    <span class="brand-sub">Custom Homes</span>
  </div>

  <span class="rule" style="left:665px;top:378px;width:95px;height:2px"></span>
  <span class="rule" style="left:697px;top:361px;width:2px;height:72px"></span>
</section>

<section class="card card--back">
  <div class="brand brand--back">
    <span class="brand-dot"></span>
    <span class="brand-name">Bright Fern</span>
    <span class="brand-sub">Custom Homes</span>
  </div>
  <p class="website">www.brightferncustomhomes.example</p>
</section>

</body>
</html>
```